Business supporting small business needs: Business card, A4 letterhead, A6 postcard, C5& C6envelope

We require stationery designed for a new Australian company called "Tallow Meadow" that provides operational strategy and support to small businesses.

We already have a logo (attached).

We require:
- business card (double-sided)
- A4 letterhead (double-sided)
- A6 postcard - to be used like a with-compliments slip (double-sided)
- C5 envelope
- C6 envelope

We would like the backs of the business card, letterhead and postcard to strongly feature the blue colour from the logo.

The business card, letterhead and postcard must contain:
- Tallow Meadow
- Staff member name
- Website address
- Email address
- Phone number
- Postal address
(I will provide these details to the winner)

The letterhead must also contain the ABN: 57 382 916 204 and company name "Tallow Meadow Pty Ltd".

Our standard font is century gothic.
Updates

Thank you for the designs so far.

Please note that the only change to the logo I am open to, is using an all white logo on a blue background.

I am not open to any other changes to the logo, such as shading, shadows or other colour changes.

Target Market(s)

Small and micro business owners

Industry/Entity Type

Small Business

```html
<!DOCTYPE html>
<html lang="en">
<head>
<meta charset="utf-8">
<title>Tallow Meadow – Envelope Stationery</title>
<link rel="stylesheet" href="https://fonts.googleapis.com/css2?family=Questrial&display=swap">
<style>
  :root {
    --brand-blue: #3aabd0;
    --brand-blue-deep: #36a2c6;
    --brand-blue-line: #5cbcdb;
    --paper: #ffffff;
    --ink-grey: #6f6f6f;
    --backdrop: #ececec;
  }
  * { margin: 0; padding: 0; box-sizing: border-box; }
  html, body {
    width: 1200px;
    height: 900px;
    overflow: hidden;
    background: var(--backdrop);
    font-family: "Questrial", "Century Gothic", sans-serif;
  }
  .stationery {
    position: relative;
    width: 1200px;
    height: 900px;
  }
  .envelope {
    position: absolute;
    overflow: hidden;
  }
  .envelope-back {
    left: 105px;
    top: 75px;
    width: 698px;
    height: 496px;
    background: var(--brand-blue);
  }
  .envelope-front {
    left: 433px;
    top: 323px;
    width: 700px;
    height: 495px;
    background: var(--paper);
  }
  .envelope-art {
    position: absolute;
    inset: 0;
    width: 100%;
    height: 100%;
  }
  .wordmark-large {
    position: absolute;
    left: 110px;
    top: 150px;
    font-size: 78px;
    line-height: 1;
    color: var(--paper);
    letter-spacing: 0.5px;
    white-space: nowrap;
  }
  .sender {
    position: absolute;
    left: 48px;
    top: 48px;
  }
  .wordmark-small {
    font-size: 25px;
    line-height: 1;
    color: var(--brand-blue);
    margin-bottom: 30px;
    white-space: nowrap;
  }
  .sender-address {
    font-style: normal;
    font-size: 13px;
    line-height: 18px;
    letter-spacing: 1px;
    color: var(--ink-grey);
  }
  .sender-web {
    display: block;
    margin-top: 5px;
    font-size: 13px;
    letter-spacing: 1px;
    font-weight: bold;
    color: var(--brand-blue);
    text-decoration: none;
  }
</style>
</head>
<body>
<main class="stationery">

  <section class="envelope envelope-back" aria-label="Envelope back">
    <svg class="envelope-art" viewBox="0 0 698 496" aria-hidden="true">
      <path d="M0,430 C120,450 250,440 380,410 C480,388 600,380 698,392 L698,410 C600,400 480,410 380,432 C250,460 120,470 0,462 Z" fill="var(--brand-blue-deep)"/>
    </svg>
    <p class="wordmark-large">Tallow Meadow</p>
  </section>

  <section class="envelope envelope-front" aria-label="Envelope front">
    <svg class="envelope-art" viewBox="0 0 700 495" aria-hidden="true">
      <path d="M0,245 C30,375 140,422 300,425 C420,428 540,380 630,378 C680,378 700,410 700,440 L700,495 L0,495 Z" fill="var(--brand-blue)"/>
      <path d="M0,395 C110,455 260,472 420,452 C520,440 620,430 700,436 L700,495 L0,495 Z" fill="var(--brand-blue-deep)"/>
      <path d="M0,395 C110,455 260,472 420,452 C520,440 620,430 700,436" fill="none" stroke="var(--brand-blue-line)" stroke-width="1"/>
    </svg>
    <div class="sender">
      <p class="wordmark-small">Tallow Meadow</p>
      <address class="sender-address">
        48 Fern Road<br>
        Ashbury Vale 4021
      </address>
      <a class="sender-web" href="#">www.tallowmeadow.com</a>
    </div>
  </section>

</main>
</body>
</html>
```